デザインのイメージですが、京都の西陣織をイメージした包装紙や箱を用いておりますので、和柄や和モダンのような和のテイストで
お願いします。
元の袋は透明です。透明の上にデザインを載せていただくイメージです。透明感を生かしたデザインでも良いですし、透明の上に色をのせて
ベタ塗りの背景にしていただいてもOKです。
※印刷の性質上グラデーションはできませんのでご注意ください。
135巾x85P(ピッチ)opcp材、1粒入りの小さな個包装のデザイン4種類の作成をお願いいたします。※現在、袋サイズに関しては微調整を行っておりますのでサイズは少し変更になる場合がございます。
赤系、黄・オレンジ系、無彩色系、黄色は金色でも可。その他色もデザインに応じて可。

弊社商品のイメージにぴったりで、蒔絵のような美しいデザインが素晴らしく選定させていただきました。
ありがとうございました。

とても素晴らしいデザインが多く、選定まで難航いたしました。
新商品開発を随時進めておりますので、またの機会によろしくお願いいたします。
ありがとうございました。

```html
<!DOCTYPE html>
<html lang="ja">
<head>
<meta charset="utf-8">
<title>個包装デザイン 展開図</title>
<link rel="stylesheet" href="https://fonts.googleapis.com/css2?family=Noto+Serif+JP:wght@500;700;900&family=Noto+Sans+JP:wght@400;500&display=swap">
<style>
  :root {
    --paper: #ffffff;
    --guide: #6b6b6b;
    --arrow: #8a8a8a;
    --seal-yellow: #d8c400;
    --lattice-pink: #f4dcd5;
    --band-grey: #e4e4e4;
    --lattice-red: #cf5b45;
    --tab-black: #2a1a17;
    --label-red: #c41a1f;
    --ink: #2b1c18;
    --white: #ffffff;
  }
  html, body { margin: 0; padding: 0; overflow: hidden; }
  body { width: 764px; height: 1200px; background: var(--paper); position: relative; font-family: "Noto Sans JP", sans-serif; }
  .sheet { position: absolute; inset: 0; width: 764px; height: 1200px; }
  .pouch { position: absolute; left: 110px; top: 165px; width: 489px; height: 850px; overflow: hidden; }
  .pouch__top { position: absolute; left: 0; top: 0; width: 100%; height: 283px; background: var(--lattice-pink); }
  .pouch__band { position: absolute; left: 0; top: 283px; width: 100%; height: 80px; background: var(--band-grey); }
  .pouch__bottom { position: absolute; left: 0; top: 363px; width: 100%; height: 487px; background: var(--lattice-red); }
  .pouch__seal { position: absolute; top: 0; height: 100%; background: var(--seal-yellow); }
  .pouch__seal--left { left: 0; width: 23px; }
  .pouch__seal--right { right: 0; width: 26px; }
  .pouch__tab { position: absolute; left: 231px; width: 28px; height: 53px; background: var(--tab-black); }
  .pouch__tab--top { top: 70px; }
  .pouch__tab--bottom { top: 715px; }
  .cracker-photo { position: absolute; left: 185px; top: 300px; width: 180px; height: 130px; border-radius: 50%;
    background: radial-gradient(ellipse at 50% 45%, #f3c27e 0%, #e19a4f 55%, rgba(225,154,79,0) 75%); }
  .grade-label { position: absolute; left: 261px; top: 255px; width: 26px; height: 110px; background: var(--label-red);
    color: var(--white); writing-mode: vertical-rl; font-family: "Noto Serif JP", serif; font-weight: 700; font-size: 13px;
    display: flex; align-items: center; justify-content: center; letter-spacing: 1px; }
  .product-name { position: absolute; left: 205px; top: 397px; width: 100px; height: 100px; border-radius: 50%; background: var(--white);
    display: flex; align-items: center; justify-content: center; font-family: "Noto Serif JP", serif; font-weight: 900; font-size: 58px; color: var(--ink); }
  .flavour { position: absolute; left: 275px; top: 520px; writing-mode: vertical-rl; color: var(--white);
    font-family: "Noto Serif JP", serif; font-weight: 700; font-size: 26px; letter-spacing: 4px; }
  .dim { position: absolute; color: var(--guide); font-size: 15px; line-height: 1; }
  .dim--side { writing-mode: vertical-rl; transform: rotate(180deg); }
  .dim--flow { left: 355px; top: 4px; writing-mode: vertical-rl; font-size: 17px; font-weight: 500; }
  .dim--width { left: 700px; top: 440px; writing-mode: vertical-rl; font-size: 19px; }
  .dim--pitch { left: 338px; top: 1100px; writing-mode: vertical-rl; font-size: 17px; }
</style>
</head>
<body>
<div class="sheet">
  <svg class="guides" width="764" height="1200" viewBox="0 0 764 1200" style="position:absolute;left:0;top:0">
    <g stroke="var(--guide)" stroke-width="1" fill="none">
      <line x1="60" y1="150" x2="60" y2="1030"/>
      <line x1="45" y1="165" x2="110" y2="165"/>
      <line x1="45" y1="228" x2="110" y2="228"/>
      <line x1="45" y1="409" x2="110" y2="409"/>
      <line x1="45" y1="771" x2="110" y2="771"/>
      <line x1="45" y1="952" x2="110" y2="952"/>
      <line x1="45" y1="1015" x2="110" y2="1015"/>
      <line x1="637" y1="165" x2="637" y2="1015"/>
      <line x1="599" y1="165" x2="660" y2="165"/>
      <line x1="599" y1="1015" x2="660" y2="1015"/>
      <line x1="110" y1="1045" x2="599" y2="1045"/>
      <line x1="110" y1="1015" x2="110" y2="1060"/>
      <line x1="599" y1="1015" x2="599" y2="1060"/>
    </g>
    <g fill="var(--arrow)">
      <rect x="140" y="78" width="430" height="6"/>
      <polygon points="118,81 145,68 145,94"/>
      <polygon points="592,81 565,68 565,94"/>
    </g>
  </svg>

  <span class="dim dim--flow">流れ方向</span>
  <span class="dim dim--side" style="left:62px;top:186px">10</span>
  <span class="dim dim--side" style="left:62px;top:296px">28.75</span>
  <span class="dim dim--side" style="left:62px;top:570px">57.5</span>
  <span class="dim dim--side" style="left:62px;top:841px">28.75</span>
  <span class="dim dim--side" style="left:62px;top:974px">10</span>
  <span class="dim dim--width">135巾</span>
  <span class="dim dim--pitch">85P</span>

  <div class="pouch">
    <div class="pouch__top" role="img" aria-label="淡い桃色の菱形格子と菱文の和柄"></div>
    <div class="pouch__band"></div>
    <div class="pouch__bottom" role="img" aria-label="朱色地に菱形格子の和柄"></div>
    <div class="cracker-photo" role="img" aria-label="醤油あられの写真"></div>
    <div class="grade-label">上代御あられ</div>
    <div class="product-name">鶴</div>
    <div class="flavour">秘伝醤油</div>
    <div class="pouch__tab pouch__tab--top"></div>
    <div class="pouch__tab pouch__tab--bottom"></div>
    <div class="pouch__seal pouch__seal--left"></div>
    <div class="pouch__seal pouch__seal--right"></div>
  </div>
</div>
</body>
</html>
```